Nobre Lente Lusitana - business card

Create a business card for my eyewear (glasses) store. The concept is based in handcrafted glasses (as well as common frames and 3d printed), clean, and elegant. The business card could be black (white letters and symbols) or white (black letters and symbols) but we are open to new suggestions. It must be sober and elegant.
The name Nobre Lente Lusitana means Royal/Real Portuguese Optical Store.
Our concept should be inspired by the pictures attatched bellow.
I would like it to be classic and elegant as business cards for bankers.
Our first selected logo is also available in attachment files.

Target Market(s)

For business meetings with investors, supliers and fairs

Industry/Entity Type

Eyewear

Contact Information for Business Card

Some random business cards in attachment that we like. Don't be closed to it, we like freedom of think.

Font styles to use
Serif
Sans Serif

Colors
404040
e9e9e9
fbfbfb
000000
85abd3
0255a3
f7fbfd
959595

Requirements
Must have
• Must be elegant, simple.
• Must present our brand new logo (slight variations are welcome, the logo is not closed yet). See our temporary logo in attachment.
• Black (or dark grey), white (or light grey) and a third slight color.
• This third slight color could be dark blue or grayish blue.
• Info:
• Tomás Vidigal (name)
• tvidigal@nobrelentelusitana.example
• +351 927364051
• www.nobrelentelusitana.example
Nice to have
• Black and white or with serious colors such as dark blue or greyish blue.
• Could also have water mark with our logo (big size) in the background (inspired in KMT bank credit card design)
Should not have
• Hysteric colora or shapes

```html
<!DOCTYPE html>
<html lang="pt">
<head>
<meta charset="utf-8">
<title>Nobre Lente Lusitana – Cartão de visita</title>
<link href="https://fonts.googleapis.com/css2?family=Roboto+Slab:wght@500;800&family=Lato:wght@400&display=swap" rel="stylesheet">
<style>
  :root {
    --backdrop: #e6eaea;
    --card: #fbfbfb;
    --ink: #000000;
    --ink-soft: #404040;
    --muted: #6e6e6e;
    --shadow: rgba(0, 0, 0, 0.12);
  }
  * { box-sizing: border-box; margin: 0; padding: 0; }
  html, body {
    width: 1200px;
    height: 900px;
    overflow: hidden;
    background: var(--backdrop);
  }
  .canvas {
    position: relative;
    width: 1200px;
    height: 900px;
  }
  .card {
    position: absolute;
    width: 560px;
    height: 320px;
    background: var(--card);
    box-shadow: 0 10px 28px var(--shadow);
  }
  .card--front { left: 150px; top: 90px; }
  .card--back  { left: 490px; top: 490px; }

  .brand {
    position: absolute;
    font-family: "Roboto Slab", serif;
    font-weight: 800;
    color: var(--ink);
    text-transform: uppercase;
    letter-spacing: 0.14em;
    font-size: 20px;
    line-height: 1.35;
  }
  .card--front .brand {
    left: 0; right: 0; top: 114px;
    text-align: center;
  }
  .card--back .brand {
    left: 56px; top: 150px;
  }

  .holder {
    position: absolute;
    left: 300px;
    right: 30px;
    top: 28px;
  }
  .rule {
    height: 2px;
    background: var(--ink);
  }
  .rule--top { margin-left: 70px; }
  .holder__name {
    font-family: "Roboto Slab", serif;
    font-weight: 800;
    font-size: 19px;
    color: var(--ink);
    text-transform: uppercase;
    letter-spacing: 0.02em;
    margin: 58px 0 16px;
  }
  .rule--bottom { margin-right: 40px; }

  .contacts {
    list-style: none;
    margin-top: 22px;
    font-family: "Lato", sans-serif;
    font-size: 13px;
    color: var(--muted);
  }
  .contacts li {
    display: flex;
    align-items: center;
    gap: 8px;
    line-height: 20px;
  }
  .contacts svg { flex: none; }
</style>
</head>
<body>
<main class="canvas">

  <section class="card card--front" aria-label="Frente do cartão">
    <p class="brand">Nobre<br>Lente<br>Lusitana</p>
  </section>

  <section class="card card--back" aria-label="Verso do cartão">
    <p class="brand">Nobre<br>Lente<br>Lusitana</p>

    <div class="holder">
      <div class="rule rule--top"></div>
      <h1 class="holder__name">Tomás Vidigal</h1>
      <div class="rule rule--bottom"></div>

      <ul class="contacts">
        <li>
          <svg width="12" height="12" viewBox="0 0 24 24" aria-hidden="true">
            <path fill="#404040" d="M6.6 10.8a15.2 15.2 0 0 0 6.6 6.6l2.2-2.2a1 1 0 0 1 1-.25 11.4 11.4 0 0 0 3.6.57 1 1 0 0 1 1 1V20a1 1 0 0 1-1 1A17 17 0 0 1 3 4a1 1 0 0 1 1-1h3.5a1 1 0 0 1 1 1c0 1.25.2 2.45.57 3.57a1 1 0 0 1-.25 1z"/>
          </svg>
          <span>+351 927364051</span>
        </li>
        <li>
          <svg width="12" height="12" viewBox="0 0 24 24" aria-hidden="true">
            <rect x="2" y="5" width="20" height="14" rx="2" fill="#404040"/>
            <path d="M3 6l9 7 9-7" fill="none" stroke="#fbfbfb" stroke-width="2"/>
          </svg>
          <span>tvidigal@nobrelentelusitana.example</span>
        </li>
        <li>
          <svg width="12" height="12" viewBox="0 0 24 24" aria-hidden="true">
            <circle cx="12" cy="12" r="10" fill="#404040"/>
            <path d="M2 12h20M12 2c3 3 3 17 0 20M12 2c-3 3-3 17 0 20" fill="none" stroke="#fbfbfb" stroke-width="1.5"/>
          </svg>
          <span>www.nobrelentelusitana.example</span>
        </li>
      </ul>
    </div>
  </section>

</main>
</body>
</html>
```